Letterhead designs for Property Management firm

Would like to see some different letterhead/envelope designs We are a residential property management company. We would like to see designs that utilize blue/grays/black

```html
<!DOCTYPE html>
<html lang="en">
<head>
<meta charset="utf-8">
<title>Northgate Property Management – Stationery</title>
<link rel="stylesheet" href="https://fonts.googleapis.com/css2?family=Lato:wght@400;700;900&display=swap">
<style>
  :root {
    --backdrop: #acacac;
    --paper: #ffffff;
    --brand-blue: #1553a6;
    --brand-black: #1d1d1d;
    --ink: #1a1a1a;
    --watermark: #e9e9e9;
    --rule-gray: #c9c9c9;
  }
  * { margin: 0; padding: 0; box-sizing: border-box; }
  html, body { width: 1200px; height: 1200px; overflow: hidden; }
  body {
    background: var(--backdrop);
    font-family: "Lato", Arial, sans-serif;
    color: var(--ink);
    position: relative;
  }
  .sheet { position: absolute; background: var(--paper); overflow: hidden; }
  .sheet svg.band { position: absolute; left: 0; display: block; }

  /* Letterhead */
  .letterhead { left: 43px; top: 115px; width: 559px; height: 722px; }
  .letterhead .top-rule { position: absolute; left: 0; top: 0; width: 100%; height: 6px; background: var(--brand-blue); }
  .brand { position: absolute; display: flex; align-items: center; gap: 6px; color: var(--brand-blue); font-weight: 900; }
  .brand .mark { background: var(--brand-blue); flex: none; }
  .brand .name { line-height: 1.05; text-transform: uppercase; }
  .brand .name span { display: block; }
  .letterhead .brand { left: 66px; top: 62px; }
  .letterhead .brand .mark { width: 22px; height: 22px; }
  .letterhead .brand .name { font-size: 19px; letter-spacing: 0.5px; }
  .letterhead .brand .name span + span { font-size: 9.5px; letter-spacing: 0.6px; }

  .contact { position: absolute; left: 383px; top: 43px; height: 60px; border-left: 1px solid var(--brand-blue); padding-left: 7px; font-size: 8.2px; color: var(--ink); }
  .contact li { list-style: none; display: flex; align-items: center; gap: 5px; height: 12.3px; }
  .contact svg { width: 8px; height: 7px; flex: none; }
  .contact address { font-style: normal; margin-top: 3px; line-height: 9px; }

  .recipient { position: absolute; left: 66px; top: 148px; font-size: 9.6px; font-weight: 700; line-height: 19.2px; }
  .body-copy { position: absolute; left: 66px; top: 244px; font-size: 9.6px; line-height: 19.2px; }
  .body-copy p + p { margin-top: 19.2px; }
  .sign-off { position: absolute; left: 66px; top: 531px; font-size: 9.6px; line-height: 19.2px; }
  .signature { position: absolute; left: 66px; top: 553px; width: 120px; height: 52px; background: linear-gradient(90deg, #f1f1f1, #fafafa); }
  .signer { position: absolute; left: 66px; top: 608px; font-size: 9.6px; line-height: 19.2px; }
  .watermark { position: absolute; background: linear-gradient(180deg, rgba(233,233,233,0.2), var(--watermark)); }

  /* Envelopes */
  .envelope-front { width: 516px; height: 231px; }
  .env-a { left: 636px; top: 115px; }
  .env-c { left: 638px; top: 626px; width: 511px; height: 229px; }
  .envelope-front .brand { left: 14px; top: 14px; gap: 3px; }
  .envelope-front .brand .mark { width: 8px; height: 8px; }
  .envelope-front .brand .name { font-size: 8px; }
  .envelope-front .brand .name span + span { font-size: 4.2px; letter-spacing: 0.2px; }
  .return-address { position: absolute; left: 14px; top: 56px; font-style: normal; font-size: 6px; line-height: 7.6px; }

  .envelope-back { left: 638px; width: 511px; height: 229px; }
  .env-b { top: 372px; }
  .env-d { top: 881px; }
  .flap { position: absolute; left: 0; top: 0; }
</style>
</head>
<body>

<!-- Letterhead -->
<section class="sheet letterhead" aria-label="Letterhead">
  <div class="top-rule"></div>

  <div class="brand">
    <span class="mark"></span>
    <div class="name"><span>Northgate</span><span>Property Management</span></div>
  </div>

  <div class="contact">
    <ul>
      <li><svg viewBox="0 0 8 7"><rect width="8" height="7" rx="1" fill="#1553a6"/><path d="M2 2.2h4M2.5 4.5h3" stroke="#fff" stroke-width="0.9"/></svg>+1 234 567 8901</li>
      <li><svg viewBox="0 0 8 7"><rect width="8" height="7" rx="1" fill="#1553a6"/><rect x="2" y="2" width="4" height="3" fill="#fff"/></svg>+1 234 567 8901</li>
      <li><svg viewBox="0 0 8 7"><rect width="8" height="7" rx="1" fill="#1553a6"/><path d="M1.5 2l2.5 2 2.5-2" stroke="#fff" stroke-width="0.8" fill="none"/></svg>emailaddress@email.com</li>
    </ul>
    <address>Address Line 1, Area<br>City Name, Area Name</address>
  </div>

  <div class="recipient">To<br>Lorem Ipsum is simply<br>Lorem Ipsum is Lorem Ipsum is<br>Lorem Ipsum is</div>

  <div class="body-copy">
    <p>&nbsp;dummy text of the printing and typesetting industry. Lorem Ipsum has been the industry's standard<br>dummy text ever since the 1500s, when an unknown printer took a galley of type and scrambled it<br>to make a type specimen book. It has survived not only five centuries, but also the leap into elec-<br>tronic typesetting, remaining essentially unchanged.</p>
    <p>It is a long established fact that a reader will be distracted by the readable content of a page when<br>looking at its layout. The point of using Lorem Ipsum is that it has a more-or-less normal distribution<br>of letters, as opposed to using 'Content here, content here', making it look like readable English.<br>Many desktop publishing packages and web page editors now use Lorem Ipsum as their default</p>
    <p>&nbsp;Contrary to popular belief, Lorem Ipsum is not simply random text. It has roots in a piece of classical<br>Latin literature from 45 BC, making it over 2000 years old. Daniel Whitcombe, a Latin professor at<br>Ashbourne Hill College in Vermont, looked up one of the more obscure Latin words, consectetur,<br>from a Lorem Ipsum passage,</p>
  </div>

  <div class="sign-off">Lorem Ipsum</div>
  <div class="signature" role="img" aria-label="Handwritten signature"></div>
  <div class="signer">Lorem Ipsum is a dummy</div>

  <div class="watermark" style="left:202px;top:605px;width:356px;height:106px;" role="img" aria-label="Faint decorative watermark"></div>

  <svg class="band" style="top:706px" width="559" height="16" viewBox="0 0 559 16">
    <polygon points="0,0 138,0 153,16 0,16" fill="#1d1d1d"/>
    <polygon points="143,8 559,8 559,16 151,16" fill="#1553a6"/>
    <line x1="140" y1="0" x2="155" y2="16" stroke="#fff" stroke-width="2"/>
  </svg>
</section>

<!-- Envelope front with band -->
<section class="sheet envelope-front env-a" aria-label="Envelope front">
  <div class="brand">
    <span class="mark"></span>
    <div class="name"><span>Northgate</span><span>Property Management</span></div>
  </div>
  <address class="return-address">Address Line 1, Area,<br>City Name, Area<br>Name 8976</address>
  <div class="watermark" style="left:272px;top:153px;width:240px;height:68px;" role="img" aria-label="Faint decorative watermark"></div>
  <svg class="band" style="top:217px" width="516" height="14" viewBox="0 0 516 14">
    <polygon points="0,0 120,0 134,14 0,14" fill="#1d1d1d"/>
    <polygon points="127,7 516,7 516,14 134,14" fill="#1553a6"/>
    <line x1="122" y1="0" x2="136" y2="14" stroke="#fff" stroke-width="2"/>
  </svg>
</section>

<!-- Envelope back, blue flap -->
<section class="sheet envelope-back env-b" aria-label="Envelope back">
  <svg class="flap" width="511" height="80" viewBox="0 0 511 80">
    <path d="M0,0 H511 L497,66 Q494,76 484,76 H27 Q17,76 14,66 Z" fill="#1553a6"/>
    <rect x="172" y="33" width="163" height="43" fill="#1d5db3" role="img" aria-label="Faint decorative watermark"/>
  </svg>
</section>

<!-- Envelope front, plain -->
<section class="sheet envelope-front env-c" aria-label="Envelope front">
  <div class="brand">
    <span class="mark"></span>
    <div class="name"><span>Northgate</span><span>Property Management</span></div>
  </div>
  <address class="return-address">Address Line 1, Area,<br>City Name, Area<br>Name 8976</address>
  <div class="watermark" style="left:210px;top:144px;width:292px;height:85px;" role="img" aria-label="Faint decorative watermark"></div>
</section>

<!-- Envelope back, white flap -->
<section class="sheet envelope-back env-d" aria-label="Envelope back">
  <svg class="flap" width="511" height="80" viewBox="0 0 511 80">
    <path d="M0,0 H511 L497,66 Q494,76 484,76 H27 Q17,76 14,66 Z" fill="#ffffff" stroke="#c9c9c9" stroke-width="1"/>
    <rect x="172" y="33" width="163" height="42" fill="#eeeeee" role="img" aria-label="Faint decorative watermark"/>
  </svg>
</section>

</body>
</html>
```